Criação de Layout de Post para Alimentos & Bebidas
A empresa queria:
" Restaurante com petiscos, a la carte, bebidas. Funcionamos a partir de 8hs da manhã, de segunda a quinta até as 23h e finais de semana até as 2h da manhã "

```html
<!DOCTYPE html>
<html lang="pt-BR">
<head>
<meta charset="UTF-8">
<title>Brasador Bar e Restaurante</title>
<link href="https://fonts.googleapis.com/css2?family=Montserrat:wght@500;600;700;800;900&display=swap" rel="stylesheet">
<style>
  :root {
    --wall-dark: #121212;
    --wall-mid: #2c2c2a;
    --wall-light: #3d3d3a;
    --card: #e8efc6;
    --card-glow: rgba(232, 239, 198, 0.35);
    --brand-green: #3b6a1f;
    --brand-brown: #9a5418;
    --gold: #c98a2b;
    --ring: #8d6a24;
    --white: #ffffff;
    --muted: #cfcfcf;
    --line: #4d6a6a;
  }
  * { margin: 0; padding: 0; box-sizing: border-box; }
  html, body {
    width: 1200px; height: 1200px; overflow: hidden;
    background: var(--wall-dark);
    font-family: 'Montserrat', Arial, sans-serif;
  }
  .post { position: relative; width: 1200px; height: 1200px; overflow: hidden; }
  .wall {
    position: absolute; inset: 0;
    background: radial-gradient(ellipse 60% 55% at 50% 38%, var(--wall-light) 0%, var(--wall-mid) 45%, var(--wall-dark) 100%);
  }
  .decor { position: absolute; inset: 0; }

  .logo-card {
    position: absolute; left: 343px; top: 132px; width: 514px; height: 510px;
    background: var(--card);
    box-shadow: 0 0 60px var(--card-glow);
  }
  .logo-mark {
    position: absolute; left: 177px; top: 108px;
    width: 160px; height: 160px; border-radius: 50%;
    background: var(--brand-brown);
  }
  .logo-name {
    position: absolute; left: 0; right: 0; top: 318px; text-align: center;
    font-weight: 800; font-size: 92px; line-height: 1; color: var(--brand-green);
  }
  .logo-tagline {
    position: absolute; left: 0; right: 0; top: 408px; text-align: center;
    font-weight: 700; font-size: 30px; line-height: 1; letter-spacing: 3px; color: var(--brand-green);
  }

  .line {
    position: absolute; left: 0; right: 0; text-align: center; line-height: 1; color: var(--white);
  }
  .invite { top: 740px; font-weight: 800; font-size: 56px; }
  .name { top: 806px; font-weight: 900; font-size: 96px; color: var(--gold); }
  .pitch { top: 925px; font-weight: 800; font-size: 26px; }
  .pitch-sub { top: 970px; font-weight: 700; font-size: 18px; }
  .hours { font-weight: 700; font-size: 20px; color: var(--muted); }
  .hours.first { top: 1036px; }
  .hours.second { top: 1066px; }

  .contacts {
    position: absolute; left: 0; right: 0; top: 1134px; height: 36px;
    display: flex; justify-content: center; align-items: center; gap: 30px;
    color: var(--white); font-weight: 600; font-size: 21px;
  }
  .contact { display: flex; align-items: center; gap: 10px; }
  .dot { width: 32px; height: 32px; border-radius: 50%; flex: none; }
  .dot.green { background: #2fb14a; }
  .dot.blue { background: #2d5fb8; }
  .dot.pink { background: #c8408a; }
</style>
</head>
<body>
<main class="post">
  <div class="wall" role="img" aria-label="Parede de tijolos escura iluminada ao centro"></div>

  <svg class="decor" width="1200" height="1200" viewBox="0 0 1200 1200" aria-hidden="true">
    <circle cx="1040" cy="70" r="64" fill="none" stroke="var(--ring)" stroke-width="26"/>
    <line x1="930" y1="170" x2="1060" y2="300" stroke="var(--line)" stroke-width="5"/>
    <line x1="965" y1="150" x2="1095" y2="280" stroke="var(--line)" stroke-width="5"/>
  </svg>

  <section class="logo-card">
    <div class="logo-mark"></div>
    <div class="logo-name">Brasador</div>
    <div class="logo-tagline">BAR E RESTAURANTE</div>
  </section>

  <p class="line invite">VENHA CONHECER O</p>
  <p class="line name">BRASADOR</p>
  <p class="line pitch">E SE DELICIAR COM UMA COMIDA MARAVILHOSA</p>
  <p class="line pitch-sub">JUNTO COM AQUELA CERVEJA OU SUCO ESTUPIDAMENTE GELADO</p>
  <p class="line hours first">SEGUNDA A QUINTA DAS 08:00 ÀS 23:00hrs</p>
  <p class="line hours second">FINAIS DE SEMANA DAS 08:00 ÀS 02:00hrs</p>

  <footer class="contacts">
    <span class="contact"><span class="dot green"></span>(71) 90000-4821</span>
    <span class="contact">(71) 3000-5174</span>
    <span class="contact"><span class="dot blue"></span>/brasadorbar</span>
    <span class="contact"><span class="dot pink"></span>@brasadorbar</span>
  </footer>
</main>
</body>
</html>
```